Are Your Sunny Petal? Innovative Company Needs a Web Design *Guaranteed*

We need a web design for our coaching company that helps college women overcome depression and anxiety without the stigma or hassle of traditional therapy. Ultimately, we need a website that conveys that we are the world's leading experts in this area. That is our focus. It must invite a very trusting and free spirited feminine atmoshpere that a college girl would cherish and would not hesitate to revist again and again. We need a balance of being the experts and being a laid-back party spot, a place where our college clients become absolute raving fans of our service and take action. It should be easy on the eyes, great to look at, and makes a awesome first impression. We would like to see the color scheme match our logo coloring as well.

Target Market(s)

College Women

Requirements
Must have
• Social media integration is vital. This webpage should also be mobile friendly, a good balance of flash and flow yet simplicity. It must follow the placement format we have provided. Arial, Verdana fonts preferred. Our objective is for them to "see what we are all about" in just a glimpse of the page, without scrolling down or actions, more specifically to draw ALL attention to watch our pitch video.
Nice to have
• Since our logo has a flower on it, Im curious to see what can be done with that coloring. Perhaps a tropic of Hawaiian theme? Plants are metaphoric for growth and are always a nice background. A pop-up upon entering page to capture emails for free content would be really nice to collect their name, cell, email, biggest challenge.
Should not have
• No ugly colors. Nothing that is to serious. And most importantly, we want to convey we are experts. The design cannot give the impression that we are some large, dark, ominous company with a shady agenda. College students do not trust companies like this especially since most are only out for their money. We want to separate ourselves from the pack and prove we are all about them and always on their side.

```html
<!DOCTYPE html>
<html lang="en">
<head>
<meta charset="utf-8">
<title>Sunny Petal – Coaching for College Women</title>
<link rel="stylesheet" href="https://fonts.googleapis.com/css2?family=Source+Sans+3:ital,wght@0,400;0,600;0,700;1,400&display=swap">
<style>
  :root {
    --pink: #ee3f8f;
    --pink-soft: #f07fae;
    --pink-pale: #fbe3ec;
    --blue: #1f6fb8;
    --blue-soft: #5aa0de;
    --blue-dark: #145a9c;
    --text: #555a60;
    --text-light: #8a8f95;
    --grey-line: #d7d7d9;
    --footer: #e7e7e9;
    --footer-top: #eeeef0;
    --plum: #9a1d55;
    --white: #ffffff;
    --dark: #1b1b1d;
    --silver: #d9dadd;
    --head-font: "Source Sans 3", Arial, sans-serif;
    --body-font: Arial, Verdana, sans-serif;
  }
  * { box-sizing: border-box; margin: 0; padding: 0; }
  html, body { width: 1195px; height: 1200px; overflow: hidden; background: #f6f6f7; }
  body { font-family: var(--body-font); color: var(--text); }
  .page { position: relative; width: 1195px; height: 1200px; overflow: hidden;
    background: linear-gradient(180deg, #fdf1f5 0%, #fbeef3 40%, #f4f3f5 62%, #efeff1 100%); }
  .abs { position: absolute; }

  .hero-backdrop { left: 0; top: 0; width: 1195px; height: 720px;
    background:
      radial-gradient(ellipse 420px 260px at 260px 300px, rgba(240,127,174,.35), transparent 70%),
      radial-gradient(ellipse 380px 200px at 120px 520px, rgba(190,160,220,.30), transparent 70%),
      radial-gradient(ellipse 500px 240px at 560px 150px, rgba(238,63,143,.16), transparent 70%); }
  .leaves { left: 1019px; top: 0; width: 176px; height: 115px; border-bottom-left-radius: 90px;
    background: radial-gradient(ellipse at 60% 40%, #b6dc52, #8cc23a 55%, rgba(140,194,58,0) 80%); }

  /* header */
  .brand { left: 166px; top: 58px; display: flex; align-items: center; gap: 12px; }
  .brand-dot { width: 46px; height: 46px; border-radius: 50%; background: var(--pink); }
  .brand-name { font-family: var(--head-font); font-weight: 600; font-size: 28px; color: var(--blue); }
  .connect { left: 566px; top: 45px; font-size: 11px; color: #8d8f93; letter-spacing: .2px; }
  .social { top: 38px; width: 22px; height: 22px; border-radius: 3px; }
  .social.s1 { left: 699px; background: #3b5b9a; }
  .social.s2 { left: 742px; background: #3fb3e0; }
  .social.s3 { left: 788px; background: #f07a1d; }
  .search { left: 842px; top: 34px; width: 177px; height: 29px; background: var(--white);
    border: 1px solid #dcdcdf; border-radius: 3px; box-shadow: inset 0 1px 2px rgba(0,0,0,.08); }
  .search svg { position: absolute; right: 8px; top: 6px; }

  .nav { top: 100px; font-family: var(--head-font); font-size: 13.5px; font-weight: 600; color: var(--pink-soft); letter-spacing: .3px; }
  .nav.active { color: var(--blue-dark); }
  .nav-sep { top: 100px; font-size: 13px; color: #b9aeb3; }
  .subnav { left: 415px; top: 132px; width: 261px; height: 29px; border-radius: 4px;
    background: linear-gradient(180deg, #f9a7c3, #f07aa4); box-shadow: 0 1px 3px rgba(200,60,110,.35);
    display: flex; align-items: center; justify-content: space-around; padding: 0 6px; }
  .subnav::before { content: ""; position: absolute; left: 123px; top: -7px; border: 7px solid transparent; border-top: 0; border-bottom-color: #f9a7c3; }
  .subnav span { font-family: var(--head-font); font-weight: 700; font-size: 11px; color: var(--white); }
  .subnav i { width: 1px; height: 16px; background: rgba(255,255,255,.55); }

  /* hero */
  .headline { left: 186px; top: 218px; font-family: var(--head-font); font-size: 26px; line-height: 31px; color: var(--pink); letter-spacing: .2px; }
  .headline strong { font-weight: 700; }
  .headline .hl-blue { color: var(--blue-soft); }
  .hero-copy { left: 188px; top: 321px; width: 345px; font-size: 13px; line-height: 23.6px; color: #5e5f64; }
  .dots { left: 423px; top: 427px; display: flex; gap: 23px; }
  .dots span { width: 7px; height: 7px; border-radius: 50%; background: #c9c3c7; }
  .dots span.on { background: var(--pink); }
  .cta { left: 209px; top: 463px; width: 276px; height: 65px; border-radius: 4px;
    background: linear-gradient(180deg, #3b93d8, #1f6fb8 60%, #1a62a6); box-shadow: 0 3px 5px rgba(30,80,140,.35); color: var(--white); }
  .cta-title { position: absolute; left: 13px; top: 11px; font-family: var(--head-font); font-weight: 600; font-size: 18.5px; }
  .cta-sub { position: absolute; left: 14px; top: 38px; font-size: 9.5px; }
  .cta-arrow { position: absolute; right: 19px; top: 18px; width: 28px; height: 28px; border-radius: 50%; background: rgba(255,255,255,.22); }

  /* monitor */
  .monitor-bezel { left: 602px; top: 188px; width: 436px; height: 261px; border-radius: 10px 10px 0 0; background: var(--dark); }
  .monitor-chin { left: 602px; top: 449px; width: 436px; height: 40px; border-radius: 0 0 6px 6px; background: linear-gradient(180deg, #eceded, #cfd0d3); }
  .monitor-stand { left: 752px; top: 489px; }
  .screen-photo { left: 621px; top: 206px; width: 216px; height: 225px; background: linear-gradient(135deg, #c9b6a4, #8d6c58 55%, #3d3b48); }
  .screen-panel { left: 837px; top: 206px; width: 182px; height: 225px; background: #f6f6f6; padding: 33px 8px 0 2px; }
  .screen-panel h3 { font-family: var(--head-font); font-weight: 600; font-size: 17px; line-height: 19px; color: #444; }
  .screen-panel p { margin-top: 12px; font-size: 10.5px; line-height: 16px; color: #666; }
  .watch { position: absolute; left: 53px; top: 148px; display: flex; align-items: center; gap: 7px; font-size: 11.5px; color: var(--blue); }
  .watch i { width: 14px; height: 14px; border-radius: 50%; border: 1px solid #999; position: relative; }
  .watch i::after { content: ""; position: absolute; left: 4px; top: 3px; border: 3.5px solid transparent; border-left: 5px solid #666; border-right: 0; }
  .monitor-shadow { left: 640px; top: 552px; width: 360px; height: 14px; border-radius: 50%; background: radial-gradient(ellipse, rgba(0,0,0,.18), transparent 70%); }

  /* features */
  .feature-band { left: 155px; top: 580px; width: 893px; height: 130px; border-radius: 14px 14px 0 0;
    background: linear-gradient(180deg, #f5f5f6, #ffffff 30%); box-shadow: 0 -1px 3px rgba(0,0,0,.05); }
  .feature-card { top: 607px; width: 198px; height: 119px; background: var(--white); border: 1px solid #d5d5d8; padding: 3px; overflow: hidden; }
  .feature-card .visual { position: absolute; top: 3px; bottom: 3px; }
  .feature-card h4 { position: absolute; top: 20px; font-family: var(--head-font); font-weight: 600; font-size: 17px; letter-spacing: .2px; }
  .feature-card p { position: absolute; top: 50px; width: 92px; font-size: 9.5px; line-height: 13.5px; color: #9a9ca0; }
  .card-1 { left: 178px; } .card-2 { left: 395px; } .card-3 { left: 613px; } .card-4 { left: 830px; }
  .card-1 h4 { left: 75px; color: var(--blue); } .card-1 p { left: 75px; }
  .card-2 h4 { left: 10px; color: #444; } .card-2 h4 em { font-style: normal; color: var(--pink); } .card-2 p { left: 10px; }
  .card-3 h4 { left: 69px; color: var(--plum); } .card-3 p { left: 69px; }
  .chevron { top: 650px; }

  /* testimonials */
  .section-title { top: 787px; font-family: var(--head-font); font-weight: 600; font-size: 20px; letter-spacing: .2px; }
  .students-title { left: 180px; color: var(--blue); } .students-title em { font-style: normal; color: var(--pink); }
  .quote-badge { left: 470px; top: 762px; }
  .avatar { left: 180px; width: 64px; height: 64px; border-radius: 50%; border: 3px solid #e2e2e4; background: linear-gradient(160deg, #a77a63, #4e3a33); }
  .quote { left: 268px; width: 418px; font-size: 11.5px; line-height: 19px; font-style: italic; color: #333; }
  .quote-by { left: 560px; width: 126px; text-align: right; font-size: 11px; color: #666; }

  /* contact */
  .contact-title { left: 728px; color: #6e6f73; }
  .contact-badge { left: 849px; top: 764px; width: 64px; height: 64px; border-radius: 50%; background: #e4e4e6; }
  .map { left: 734px; top: 844px; width: 122px; height: 84px; border: 1px solid #d4d4d6; background: linear-gradient(135deg, #efe7d4, #e2d7bd); }
  .address { left: 876px; top: 847px; font-size: 10.5px; line-height: 19.4px; color: #555; }
  .contact-rule { left: 734px; top: 962px; width: 2px; height: 48px; background: #c9c9cc; }
  .phone-line { left: 765px; top: 958px; display: flex; align-items: center; gap: 12px; font-family: var(--head-font); font-weight: 600; font-size: 23px; color: var(--pink); }
  .mail-line { left: 765px; top: 993px; display: flex; align-items: center; gap: 12px; font-size: 13px; color: var(--blue); }

  .content-shadow { left: 130px; top: 1050px; width: 940px; height: 12px; border-radius: 50%; background: radial-gradient(ellipse, rgba(0,0,0,.10), transparent 70%); }

  /* footer */
  .footer { left: 124px; top: 1122px; width: 953px; height: 78px; background: var(--footer); }
  .footer-top { position: absolute; left: 0; top: 0; width: 100%; height: 28px; background: var(--footer-top);
    display: flex; justify-content: flex-end; align-items: center; gap: 14px; padding-right: 20px; font-size: 11.5px; color: #555; }
  .footer-top i { font-style: normal; color: #aaa; font-size: 10px; }
  .footer-info { position: absolute; left: 30px; top: 38px; font-size: 10.5px; color: #777; display: flex; gap: 20px; }
  .footer-info a { color: var(--blue-soft); text-decoration: none; }
  .copyright { position: absolute; left: 30px; top: 58px; font-size: 9px; color: #999; }
  .family-site { position: absolute; left: 815px; top: 39px; width: 108px; height: 18px; border-radius: 9px; background: var(--white);
    border: 1px solid #d6d6d8; font-size: 9px; color: #777; padding: 3px 0 0 10px; }
  .family-site::after { content: ""; position: absolute; right: 10px; top: 6px; border: 3px solid transparent; border-bottom: 4px solid #888; border-top: 0; }
</style>
</head>
<body>
<div class="page">
  <div class="abs hero-backdrop" role="img" aria-label="Soft flowing pink and lavender ribbon waves with sparkles"></div>
  <div class="abs leaves" role="img" aria-label="Green leafy branch reaching in from the top corner"></div>

  <header>
    <div class="abs brand"><span class="brand-dot"></span><span class="brand-name">Sunny Petal</span></div>
    <span class="abs connect">CONNECT WITH US ON</span>
    <span class="abs social s1" aria-label="Social network one"></span>
    <span class="abs social s2" aria-label="Social network two"></span>
    <span class="abs social s3" aria-label="Blog"></span>
    <div class="abs search">
      <svg width="16" height="16" viewBox="0 0 16 16"><circle cx="6.5" cy="6.5" r="4.5" fill="none" stroke="#555" stroke-width="2"/><line x1="10" y1="10" x2="14.5" y2="14.5" stroke="#555" stroke-width="2.4" stroke-linecap="round"/></svg>
    </div>

    <nav>
      <span class="abs nav active" style="left:420px">HOME</span>
      <span class="abs nav-sep" style="left:484px">/</span>
      <span class="abs nav" style="left:517px">PRODUCT</span>
      <span class="abs nav-sep" style="left:594px">/</span>
      <span class="abs nav" style="left:630px">PARENTS</span>
      <span class="abs nav-sep" style="left:703px">/</span>
      <span class="abs nav" style="left:728px">HOW IT WORKS</span>
      <span class="abs nav-sep" style="left:836px">/</span>
      <span class="abs nav" style="left:861px">ABOUT US</span>
      <span class="abs nav-sep" style="left:945px">/</span>
      <span class="abs nav" style="left:972px">CONTACT</span>
      <div class="abs subnav"><span>PRODUCT 1</span><i></i><span>PRODUCT 2</span><i></i><span>PRODUCT 3</span></div>
    </nav>
  </header>

  <section class="hero">
    <h1 class="abs headline">
      <strong>HELPING COLLEGE WOMEN</strong><br>
      KICK <span class="hl-blue">DEPRESSION</span> AND <span class="hl-blue">ANXIETY</span><br>
      FOR GOOD
    </h1>
    <p class="abs hero-copy">Lorem ipsum dolor sit amet conse ctetur adipisicing elit, sed do eiusmod tempor incididunt ut labore et dolore magna aliqua. Ut enim ad minim veniam, quis nostrud. Lorem ipsum dolor sit amet conse ctetur adipisicing elit.</p>
    <div class="abs dots"><span class="on"></span><span></span><span></span><span></span></div>
    <a class="abs cta">
      <span class="cta-title">Schedule an Appointment</span>
      <span class="cta-sub">Get Started in Seconds.</span>
      <span class="cta-arrow"><svg width="28" height="28" viewBox="0 0 28 28"><path d="M12 8 L18 14 L12 20" fill="none" stroke="#fff" stroke-width="3" stroke-linecap="round" stroke-linejoin="round"/></svg></span>
    </a>

    <div class="abs monitor-shadow"></div>
    <div class="abs monitor-bezel"></div>
    <div class="abs monitor-chin"></div>
    <svg class="abs monitor-stand" width="140" height="69" viewBox="0 0 140 69">
      <defs><linearGradient id="standGrad" x1="0" x2="1"><stop offset="0" stop-color="#c4c5c8"/><stop offset=".5" stop-color="#f1f1f2"/><stop offset="1" stop-color="#bfc0c3"/></linearGradient></defs>
      <path d="M22 0 H118 L128 60 Q130 67 120 67 H20 Q10 67 12 60 Z" fill="url(#standGrad)"/>
    </svg>
    <div class="abs screen-photo" role="img" aria-label="Video still of a smiling student in glasses holding books"></div>
    <div class="abs screen-panel">
      <h3>Maya’s Experience<br>with Sunny Petal</h3>
      <p>Lorem ipsum dolor sit amet conse ctetur adipisicing elit, sed do eiusmod.</p>
      <span class="watch"><i></i>Watch the video</span>
    </div>
  </section>

  <section class="features">
    <div class="abs feature-band"></div>
    <svg class="abs chevron" style="left:134px" width="22" height="30" viewBox="0 0 22 30"><path d="M18 3 L6 15 L18 27" fill="none" stroke="#c8c8cb" stroke-width="5"/></svg>
    <svg class="abs chevron" style="left:1048px" width="22" height="30" viewBox="0 0 22 30"><path d="M4 3 L16 15 L4 27" fill="none" stroke="#c8c8cb" stroke-width="5"/></svg>

    <article class="abs feature-card card-1">
      <div class="visual" role="img" aria-label="Photo of a smiling young woman" style="left:3px;width:66px;background:linear-gradient(90deg,#d9c2ae,#f3ece6 90%,#fff)"></div>
      <h4>BIG BENEFIT</h4>
      <p>Lorem ipsum dolor sit amet conse ctetur adipis-icing elit,</p>
    </article>
    <article class="abs feature-card card-2">
      <div class="visual" role="img" aria-label="Clock and calendar with a red rose" style="right:3px;width:88px;background:linear-gradient(135deg,#f4f4f4,#d8d8da 60%,#b8353a)"></div>
      <h4>AUTO<em>ROTATE</em></h4>
      <p>Lorem ipsum dolor sit amet conse ctetur adipisicing elit,</p>
    </article>
    <article class="abs feature-card card-3">
      <div class="visual" role="img" aria-label="Open laptop computer" style="left:3px;width:60px;background:linear-gradient(135deg,#ffffff,#c9ccd2 60%,#7a7f88)"></div>
      <h4>BAR LAYOUTS</h4>
      <p>Lorem ipsum dolor sit amet conse ctetur adipisicing elit,</p>
    </article>
    <article class="abs feature-card card-4">
      <div class="visual" role="img" aria-label="Photo of a student smiling at her laptop" style="left:3px;right:3px;background:linear-gradient(135deg,#c6c0bc,#8f7464 50%,#e4e2e0)"></div>
    </article>
  </section>

  <section class="testimonials">
    <h2 class="abs section-title students-title">WHAT STUDENTS <em>ARE SAYING</em></h2>
    <svg class="abs quote-badge" width="71" height="68" viewBox="0 0 71 68">
      <path d="M35 2 C54 2 69 15 69 31 C69 47 54 60 35 60 L26 67 L26 58 C12 54 2 44 2 31 C2 15 16 2 35 2 Z" fill="#f6b3cc"/>
      <text x="35" y="50" text-anchor="middle" font-family="Arial, sans-serif" font-weight="700" font-size="44" fill="#ffffff">”</text>
    </svg>

    <div class="abs avatar" style="top:849px" role="img" aria-label="Portrait of a student"></div>
    <p class="abs quote" style="top:857px">“ Lorem ipsum dolor sit amet, consec tetuer adipicing it. Praesent vestibulum moles-tie lacusnen ummyhe. Odrerit mauris. Phasellus portacecipit”</p>
    <span class="abs quote-by" style="top:897px">- Lorem Ipsum</span>

    <div class="abs avatar" style="top:925px" role="img" aria-label="Portrait of a student"></div>
    <p class="abs quote" style="top:934px">“ Lorem ipsum dolor sit amet, consec tetuer adipicing it. Praesent vestibulum moles-tie lacusnen ummyhe. Odrerit mauris. Phasellus portacecipit”</p>
    <span class="abs quote-by" style="top:973px">- Lorem Ipsum</span>
  </section>

  <section class="contact">
    <h2 class="abs section-title contact-title">CONTACT US</h2>
    <div class="abs contact-badge">
      <svg width="64" height="64" viewBox="0 0 64 64"><path d="M22 18 C19 20 18 24 20 29 C24 38 30 44 38 47 C42 48 45 47 47 44 L42 38 L37 41 C33 39 28 34 26 30 L29 25 Z" fill="#ffffff"/></svg>
    </div>
    <div class="abs map" role="img" aria-label="Street map with a location pin"></div>
    <p class="abs address">Address Line 1<br>Address Line 2<br>Mon.-Fri. : 09:00 am~ 05:00 pm<br>Sat.: 09.00 am ~ 05:00 pm</p>
    <div class="abs contact-rule"></div>
    <div class="abs phone-line">
      <svg width="17" height="14" viewBox="0 0 17 14"><path d="M1 4 Q8.5 -1 16 4 L14 6 L11 4.5 L11 3 Q8.5 2 6 3 L6 4.5 L3 6 Z" fill="#a5a6aa"/><rect x="4" y="7" width="9" height="6" rx="1" fill="#a5a6aa"/></svg>
      <span>1.800.555.0142</span>
    </div>
    <div class="abs mail-line">
      <svg width="17" height="12" viewBox="0 0 17 12"><rect x="0" y="0" width="17" height="12" rx="1" fill="#a5a6aa"/><path d="M1 1 L8.5 7 L16 1" fill="none" stroke="#fff" stroke-width="1.4"/></svg>
      <span>talktous@sunnypetal.com</span>
    </div>
  </section>

  <div class="abs content-shadow"></div>

  <footer class="abs footer">
    <div class="footer-top"><span>Terms &amp; Conditions</span><i>|</i><span>Privacy</span><i>|</i><span>Contact Us</span></div>
    <div class="footer-info"><span>Address Line 1, Address Line 2</span><span>+1.800.555.0142</span><a>talktous@sunnypetal.com</a></div>
    <span class="copyright">Copyright 2013 Sunny Petal</span>
    <span class="family-site">Family Site</span>
  </footer>
</div>
</body>
</html>
```